Banner Design for High End Jewelry Website

We need a banner for our website (brindlestone.com) for a sale that we will be running. The banner should be a size 1187 × 400. I have included a few pieces of jewelry to be included in the banner (do not need to use all, can use just some). The banner should say:
"Christmas is Closer Than You Think Sale!"
Shop Now

Industry/Entity Type

Jewelry

```html
<!DOCTYPE html>
<html lang="en">
<head>
<meta charset="utf-8">
<title>Brindlestone – Christmas Sale Banner</title>
<link href="https://fonts.googleapis.com/css2?family=Pacifico&family=Roboto:wght@300;500&display=swap" rel="stylesheet">
<style>
  :root {
    --page-bg: #ffffff;
    --frame: #9a9a9a;
    --blush: #f6e6de;
    --blush-mid: #f2cfc5;
    --coral: #f47e74;
    --sale-red: #ff1a1a;
    --deep-red: #ff0d0d;
    --rose: #f7a7a7;
    --rose-light: #f1c3c3;
    --white: #ffffff;
    --ink-red: #5a0a0a;
    --button-red: #ff0000;
    --gold-light: #f3dc92;
    --gold: #d3a53a;
    --gold-deep: #9c6f18;
  }
  * { box-sizing: border-box; margin: 0; padding: 0; }
  html, body {
    width: 1200px;
    height: 692px;
    overflow: hidden;
    background: var(--page-bg);
  }
  .stage {
    position: relative;
    width: 1200px;
    height: 692px;
  }
  .banner {
    position: absolute;
    left: 86.5px;
    top: 86.5px;
    width: 1187px;
    height: 400px;
    transform: scale(0.865);
    transform-origin: top left;
    border: 1px solid var(--frame);
    box-shadow: 0 3px 6px rgba(0,0,0,0.25);
    overflow: hidden;
    background: linear-gradient(90deg,
      var(--blush) 0%,
      var(--blush-mid) 45%,
      var(--coral) 53%,
      var(--sale-red) 61%,
      var(--deep-red) 80%,
      var(--rose) 89%,
      var(--rose-light) 96%,
      var(--rose-light) 100%);
  }
  .jewelry-photo {
    position: absolute;
    left: 105px;
    top: 28px;
    width: 415px;
    height: 368px;
    border-radius: 45% 45% 30% 30%;
    background: radial-gradient(ellipse at 45% 55%,
      var(--gold-light) 0%,
      var(--gold) 45%,
      var(--gold-deep) 70%,
      rgba(156,111,24,0) 100%);
    opacity: 0.85;
  }
  .flurry {
    position: absolute;
    inset: 0;
    width: 1187px;
    height: 400px;
  }
  .flurry use { color: var(--white); opacity: 0.45; }
  .offer {
    position: absolute;
    left: 648px;
    top: 55px;
    width: 400px;
    text-align: center;
    color: var(--white);
  }
  .offer-title {
    font-family: "Pacifico", cursive;
    font-weight: 400;
    font-size: 58px;
    line-height: 80px;
    text-shadow: 1px 2px 3px rgba(90,0,0,0.45);
  }
  .offer-tagline {
    font-family: "Roboto", sans-serif;
    font-weight: 300;
    font-size: 24px;
    line-height: 30px;
    color: var(--ink-red);
    margin-top: -6px;
  }
  .offer-sale {
    display: flex;
    align-items: center;
    justify-content: center;
    gap: 18px;
    margin-top: 12px;
    font-family: "Roboto", sans-serif;
    font-weight: 500;
    font-size: 56px;
    line-height: 56px;
  }
  .offer-sale svg { width: 42px; height: 42px; color: var(--white); }
  .shop-now {
    position: absolute;
    left: 752px;
    top: 280px;
    width: 181px;
    height: 60px;
    border: 1px solid var(--white);
    background: var(--button-red);
    color: var(--white);
    font-family: "Roboto", sans-serif;
    font-weight: 500;
    font-size: 26px;
    line-height: 58px;
    text-align: center;
    text-decoration: none;
  }
</style>
</head>
<body>
<div class="stage">
  <section class="banner" aria-label="Christmas sale banner">
    <svg width="0" height="0" style="position:absolute">
      <defs>
        <symbol id="snowflake" viewBox="-20 -20 40 40">
          <g fill="none" stroke="currentColor" stroke-width="2.4" stroke-linecap="round">
            <g id="arm">
              <line x1="0" y1="0" x2="0" y2="-18"/>
              <polyline points="-5,-15 0,-10 5,-15"/>
              <polyline points="-4,-7 0,-4 4,-7"/>
            </g>
            <use href="#arm" transform="rotate(60)"/>
            <use href="#arm" transform="rotate(120)"/>
            <use href="#arm" transform="rotate(180)"/>
            <use href="#arm" transform="rotate(240)"/>
            <use href="#arm" transform="rotate(300)"/>
          </g>
        </symbol>
      </defs>
    </svg>

    <div class="jewelry-photo" role="img" aria-label="Gold cocktail rings with cabochon gemstones and a pair of diamond-set earrings"></div>

    <svg class="flurry" aria-hidden="true">
      <use href="#snowflake" x="720" y="8" width="20" height="20"/>
      <use href="#snowflake" x="820" y="42" width="20" height="20"/>
      <use href="#snowflake" x="653" y="55" width="20" height="20"/>
      <use href="#snowflake" x="975" y="23" width="20" height="20"/>
      <use href="#snowflake" x="1078" y="122" width="20" height="20"/>
      <use href="#snowflake" x="775" y="252" width="20" height="20"/>
      <use href="#snowflake" x="980" y="258" width="20" height="20"/>
      <use href="#snowflake" x="1126" y="257" width="20" height="20"/>
      <use href="#snowflake" x="640" y="322" width="20" height="20"/>
      <use href="#snowflake" x="775" y="359" width="20" height="20"/>
      <use href="#snowflake" x="895" y="348" width="20" height="20"/>
    </svg>

    <div class="offer">
      <h1 class="offer-title">Christmas</h1>
      <p class="offer-tagline">IS CLOSER THAN YOU THINK</p>
      <p class="offer-sale">
        <svg aria-hidden="true"><use href="#snowflake"/></svg>
        <span>SALE</span>
        <svg aria-hidden="true"><use href="#snowflake"/></svg>
      </p>
    </div>

    <a class="shop-now" href="#">SHOP NOW</a>
  </section>
</div>
</body>
</html>
```